Fun, Bright Company needs Packaging Design for Tin Box!

Hello! We are looking for a design for a tin box (template attached.)
This tin box will hold a set of 3 bath bombs. On the top of the box, there should be text that reads "Fizz, Darling". On the back of the box, the details should read "Set of 3 bath bombs", "Reusable tin!", have a barcode place holder, and have our logo (also attached).
This product is able to be print in full color,.
You can see our design inspiration here: https://www.quilboard.com/moonferns/design-inspo/

```html
<!DOCTYPE html>
<html lang="en">
<head>
<meta charset="utf-8">
<title>Fizz, Darling – Tin Box Packaging</title>
<link rel="stylesheet" href="https://fonts.googleapis.com/css2?family=Dancing+Script:wght@700&family=Kalam:wght@700&family=Pacifico&display=swap">
<style>
  :root {
    --paper: #ffffff;
    --hot-pink: #ff0a55;
    --deep-ink: #1b1b1b;
    --wine: #6a0f2c;
    --mint: #86c9b0;
    --sky: #a8dde0;
    --lilac: #a98bbf;
    --candy: #f06aa0;
    --candy-edge: #e8104f;
    --lid-script: #ee6aa0;
    --label-white: #ffffff;
    --label-ink: #111111;
  }
  html, body {
    margin: 0;
    padding: 0;
    width: 1200px;
    height: 1016px;
    overflow: hidden;
    background: var(--paper);
  }
  .canvas {
    position: relative;
    width: 1200px;
    height: 1016px;
  }

  /* Lid */
  .lid {
    position: absolute;
    left: 360px;
    top: 48px;
    width: 496px;
    height: 326px;
    overflow: hidden;
  }
  .lid-pattern {
    position: absolute;
    inset: 0;
    background: radial-gradient(ellipse at 50% 50%, var(--deep-ink) 0%, #3a1020 40%, #b0123f 75%, var(--hot-pink) 100%);
  }
  .lid-title {
    position: absolute;
    inset: 0;
    margin: 0;
    display: flex;
    flex-direction: column;
    align-items: center;
    justify-content: center;
    font-family: "Dancing Script", "Pacifico", cursive;
    font-weight: 700;
    font-size: 94px;
    line-height: 0.88;
    color: var(--lid-script);
    text-align: center;
  }
  .lid-title .line-one { margin-right: 40px; }
  .lid-title .line-two { margin-left: 50px; }

  /* Side flaps */
  .flap { position: absolute; }
  .flap-top {
    left: 383px; top: 433px; width: 434px; height: 132px;
    background: linear-gradient(to bottom, var(--hot-pink), var(--wine) 55%, var(--deep-ink));
  }
  .flap-bottom {
    left: 383px; top: 832px; width: 434px; height: 133px;
    background: linear-gradient(to top, var(--hot-pink), var(--wine) 55%, var(--deep-ink));
  }
  .flap-left {
    left: 250px; top: 565px; width: 133px; height: 267px;
    background: linear-gradient(to left, var(--deep-ink), var(--wine) 45%, var(--hot-pink));
  }
  .flap-right {
    left: 817px; top: 565px; width: 133px; height: 267px;
    background: linear-gradient(to right, var(--deep-ink), var(--wine) 45%, var(--hot-pink));
  }

  /* Back panel */
  .back-panel {
    position: absolute;
    left: 383px; top: 565px; width: 434px; height: 267px;
    background: var(--deep-ink);
    box-shadow: inset 0 0 0 1px #2c2c2c;
  }
  .brand-name {
    position: absolute;
    left: 0; right: 0; top: 22px;
    margin: 0;
    text-align: center;
    font-family: "Pacifico", cursive;
    font-weight: 400;
    font-size: 44px;
    line-height: 1.2;
    color: var(--mint);
  }
  .product-line {
    position: absolute;
    left: 0; right: 0; top: 92px;
    margin: 0;
    text-align: center;
    font-family: "Pacifico", cursive;
    font-size: 30px;
    line-height: 1.2;
    color: var(--sky);
  }
  .badge {
    position: absolute;
    left: 85px; top: 152px;
    width: 94px; height: 92px;
  }
  .badge-text {
    font-family: "Pacifico", cursive;
    font-size: 13px;
    fill: #ffffff;
  }
  .heart-lilac { position: absolute; left: 195px; top: 159px; width: 39px; height: 34px; }
  .heart-mint { position: absolute; left: 225px; top: 200px; width: 28px; height: 26px; }
  .barcode-slot {
    position: absolute;
    left: 290px; top: 178px;
    width: 108px; height: 61px;
    background: var(--label-white);
    display: flex;
    align-items: center;
    justify-content: center;
    font-family: "Kalam", sans-serif;
    font-weight: 700;
    font-size: 19px;
    color: var(--label-ink);
    letter-spacing: 0.5px;
  }
</style>
</head>
<body>
<main class="canvas">
  <section class="lid">
    <div class="lid-pattern" role="img" aria-label="Concentric wavy line pattern in hot pink and black radiating from the centre"></div>
    <h1 class="lid-title"><span class="line-one">Fizz,</span><span class="line-two">Darling</span></h1>
  </section>

  <div class="flap flap-top"></div>
  <div class="flap flap-left"></div>
  <div class="flap flap-right"></div>
  <div class="flap flap-bottom"></div>

  <section class="back-panel">
    <h2 class="brand-name">Glow Guild</h2>
    <p class="product-line">Set of 3 bath bombs</p>

    <svg class="badge" viewBox="0 0 94 90" aria-label="Reusable tin!">
      <path d="M47 88 C20 66 2 50 4 28 C6 10 24 2 38 10 C42 12 45 16 47 20 C50 10 62 0 76 4 C92 8 94 28 88 42 C80 60 62 74 47 88 Z" fill="var(--candy-edge)"/>
      <path d="M44 80 C20 62 6 48 8 29 C10 14 25 7 37 14 C41 16 43 19 45 22 C48 13 59 5 72 9 C86 13 87 29 82 41 C75 57 59 69 44 80 Z" fill="var(--candy)"/>
      <g transform="rotate(-18 46 42)">
        <text class="badge-text" x="46" y="38" text-anchor="middle">Reusable</text>
        <text class="badge-text" x="46" y="54" text-anchor="middle">tin!</text>
      </g>
    </svg>
    <svg class="heart-lilac" viewBox="0 0 37 33" aria-hidden="true">
      <path d="M18 32 C6 22 0 16 1 9 C2 3 9 0 14 3 C16 4 17 6 18 8 C20 3 26 0 31 2 C37 5 37 13 33 19 C29 24 24 28 18 32 Z" fill="var(--lilac)"/>
    </svg>
    <svg class="heart-mint" viewBox="0 0 28 26" aria-hidden="true">
      <path d="M14 25 C5 18 0 13 1 7 C2 2 8 0 11 3 C12 4 13 5 14 7 C15 3 20 0 24 2 C28 4 28 10 25 14 C22 18 18 21 14 25 Z" fill="var(--mint)"/>
    </svg>

    <div class="barcode-slot">BAR CODE</div>
  </section>
</main>
</body>
</html>
```